Bright Feather Glow Masterclass

This book accompanies a video workshop. The book explains who our guardian angels are, what is their purpose, how to connect with them for wisdom & guidance. How to manifest what we world like bring into our lives by asking the Angels. The book contains meditation exercises, lots of information and fun facts about how our angels give us messages and guidance and how to become more intuitive. How to use angel oracle cards to receive guidance from our angels.
I'm quite an upbeat, happy person, so the book is written very warmly and is a collection of all the information that out ther, drawn together neatly by me, with my own unique take on all things angelic. Along with personal stories and anecdotes about how and why I became interested in angels and what they have taught me. It's fun, fresh, lighthearted and modern. Not at all serious, just extremely uplifting and positive, so I would really like the cover to reflect this.
Updates

Target Market(s)

Anyone who is interested in angels. From my loopnest page activity I find it is mostly women of all ages who are interested in angels

Font styles to use
Serif
Sans Serif
Script

Colors
ea8dbb
f04a50
e667a6
e34197
85abd2
886aae
b7a5cd
6b449b
fbee3e

Requirements
Must have
• A more feminine appeal
• Look quite modern & upbeat but also calming and open
• I would like it to look etherel in some way. I definitely dont want something that looks like a cartoon or clip art
Should not have
• No dark colours or sinister imagery. I don't want people to feel like thus can't do the & it's only special people who can connect with their angels
• No haunting imagery!

```html
<!DOCTYPE html>
<html lang="en">
<head>
<meta charset="utf-8">
<title>Bright Feather Glow Masterclass – Book Cover</title>
<link rel="stylesheet" href="https://fonts.googleapis.com/css2?family=EB+Garamond:ital,wght@0,400;1,400&family=Great+Vibes&display=swap">
<style>
  :root {
    --page-bg: #ffffff;
    --peach: #f6a98f;
    --blush: #ea8dbb;
    --rose: #e667a6;
    --magenta: #e34197;
    --berry: #b81f6e;
    --veil: rgba(255, 236, 244, 0.55);
    --ink-light: #ffffff;
    --glow: rgba(120, 20, 70, 0.35);
  }
  * { margin: 0; padding: 0; box-sizing: border-box; }
  html, body {
    width: 1200px;
    height: 1000px;
    overflow: hidden;
    background: var(--page-bg);
  }
  .canvas {
    position: relative;
    width: 1200px;
    height: 1000px;
    display: flex;
    align-items: center;
    justify-content: center;
  }
  .book-cover {
    position: relative;
    width: 660px;
    height: 856px;
    overflow: hidden;
    color: var(--ink-light);
    text-align: center;
    font-family: "EB Garamond", Georgia, serif;
  }
  .cover-art {
    position: absolute;
    inset: 0;
    background:
      radial-gradient(ellipse 34% 48% at 46% 52%, var(--veil), transparent 70%),
      radial-gradient(ellipse 30% 44% at 18% 48%, rgba(255, 220, 232, 0.45), transparent 72%),
      radial-gradient(ellipse 30% 44% at 80% 46%, rgba(255, 220, 232, 0.40), transparent 72%),
      linear-gradient(125deg, var(--peach) 0%, var(--blush) 30%, var(--rose) 58%, var(--magenta) 80%, var(--berry) 100%);
  }
  .cover-text { position: absolute; inset: 0; text-shadow: 0 2px 6px var(--glow); }
  .tagline {
    position: absolute;
    top: 28px;
    left: 0;
    right: 0;
    font-style: italic;
    font-size: 21px;
    line-height: 29px;
  }
  .title-lead {
    position: absolute;
    top: 292px;
    left: 300px;
    font-size: 34px;
    line-height: 1;
  }
  .title-script {
    position: absolute;
    left: 0;
    right: 0;
    font-family: "Great Vibes", cursive;
    font-size: 132px;
    line-height: 1;
  }
  .title-script--first { top: 318px; left: 60px; }
  .title-script--second { top: 432px; left: -10px; }
  .title-tail {
    position: absolute;
    top: 560px;
    left: 0;
    right: 0;
    font-size: 40px;
    line-height: 1;
  }
  .author {
    position: absolute;
    bottom: 44px;
    left: 0;
    right: 0;
    font-size: 42px;
    line-height: 1;
  }
</style>
</head>
<body>
<main class="canvas">
  <article class="book-cover">
    <div class="cover-art" role="img" aria-label="Soft painted angel with flowing gown and wide spread wings in blush pink and magenta haze"></div>
    <div class="cover-text">
      <p class="tagline">Connect with your angels,<br>bring love, healing and divine guidance<br>to every area of your life</p>
      <h1>
        <span class="title-lead">Bright</span>
        <span class="title-script title-script--first">Feather</span>
        <span class="title-script title-script--second">Glow</span>
        <span class="title-tail">masterclass</span>
      </h1>
      <p class="author">Marisol Vantree</p>
    </div>
  </article>
</main>
</body>
</html>
```